Pathways to Brightmoor Land Ventures

size of the ad - 8”x 10.75" plus 0.25" bleed
I would like an ad for a magazine that will stand out and make people want to read the ad.
The ad should not be crowded and people reading the ad will be able to read the text.
I would like it to be a creative and modern-day design.
the list of topics should not be the focus of the ad.
the text is attached.
If you decide to use people in the ad then please no ladies.
please note that leave over 1 inch for the bottom of the footer

```html
<!DOCTYPE html>
<html lang="en">
<head>
<meta charset="utf-8">
<title>Real Estate Course – Pathways to Brightmoor Land Ventures</title>
<link href="https://fonts.googleapis.com/css2?family=Oswald:wght@300;400;600&family=Lora:wght@400;600;700&display=swap" rel="stylesheet">
<style>
  :root {
    --navy-deep: #18222f;
    --navy: #222d3d;
    --navy-light: #2a3648;
    --cyan: #5cc4dc;
    --white: #ffffff;
    --paper: #ffffff;
    --stage: #f2f3f5;
  }
  * { margin: 0; padding: 0; box-sizing: border-box; }
  html, body { width: 1200px; height: 1200px; overflow: hidden; background: var(--stage); }
  .ad {
    position: absolute; left: 135px; top: 0;
    width: 930px; height: 1200px;
    background: var(--paper);
  }
  .hero {
    position: absolute; left: 0; top: 0; width: 930px; height: 1091px;
    background: linear-gradient(160deg, var(--navy-light) 0%, var(--navy) 45%, var(--navy-deep) 100%);
    color: var(--white);
  }
  .hero-backdrop { position: absolute; inset: 0; }
  .title {
    position: absolute; left: 86px; top: 62px;
    font-family: "Oswald", sans-serif; font-weight: 600;
    font-size: 148px; line-height: 136px; letter-spacing: 0;
    text-transform: uppercase;
  }
  .subtitle {
    position: absolute; left: 86px; top: 330px;
    font-family: "Oswald", sans-serif; font-weight: 300;
    font-size: 76px; line-height: 75px; color: var(--cyan);
    text-transform: uppercase;
  }
  .tagline {
    position: absolute; left: 88px; top: 492px;
    font-family: "Lora", serif; font-weight: 400;
    font-size: 45px; line-height: 45px; text-transform: uppercase;
  }
  .details {
    position: absolute; left: 0; top: 654px; width: 437px;
    text-align: right; font-family: "Lora", serif;
  }
  .details .city { color: var(--cyan); font-weight: 700; font-size: 33px; line-height: 38px; }
  .details .strong { font-weight: 700; font-size: 27px; line-height: 31px; }
  .details .light { font-size: 21px; line-height: 26px; }
  .divider {
    position: absolute; left: 463px; top: 654px; width: 2px; height: 154px;
    background: var(--cyan);
  }
  .offer {
    position: absolute; left: 489px; top: 676px; width: 300px;
    font-family: "Lora", serif;
  }
  .offer .offer-title { color: var(--cyan); font-weight: 700; font-size: 23px; line-height: 30px; margin-bottom: 4px; }
  .offer p { font-size: 20px; line-height: 25px; }
  .topics-heading {
    position: absolute; left: 0; width: 930px; top: 880px; text-align: center;
    font-family: "Oswald", sans-serif; font-weight: 400; font-size: 21px;
    text-transform: uppercase;
  }
  .topics {
    position: absolute; top: 926px; list-style: none;
    font-family: "Lora", serif; font-size: 18px; line-height: 30.3px;
  }
  .topics.col-left { left: 148px; }
  .topics.col-right { left: 539px; }
  .topics li { display: flex; align-items: center; gap: 8px; }
  .topics svg { width: 12px; height: 12px; flex: none; }
</style>
</head>
<body>
  <div class="ad">
    <section class="hero">
      <div class="hero-backdrop" role="img" aria-label="Upward view of glass office towers in dark navy tones"></div>

      <h1 class="title">Real Estate<br>Course</h1>
      <h2 class="subtitle">Pathways to Brightmoor<br>Land Ventures</h2>
      <p class="tagline">Investing in knowledge<br>is investing in opportunities.</p>

      <div class="details">
        <p class="city">LARKFIELD</p>
        <p class="strong">10 -Tuesday</p>
        <p class="light">evenings sessions</p>
        <p class="strong">Starting Feb.28</p>
        <p class="light">Limited Partial Scholarships</p>
      </div>
      <div class="divider"></div>
      <div class="offer">
        <p class="offer-title">Early Bird Special</p>
        <p>For those that started or<br>would like to go into<br>real estate</p>
      </div>

      <p class="topics-heading">Topics: Partial Listing</p>
      <ul class="topics col-left">
        <li><svg viewBox="0 0 12 12"><circle cx="6" cy="6" r="5" fill="none" stroke="#fff" stroke-width="1"/><path d="M3.6 6.2l1.7 1.6 3.2-3.4" fill="none" stroke="#fff" stroke-width="1"/></svg>Real estate investment strategies</li>
        <li><svg viewBox="0 0 12 12"><circle cx="6" cy="6" r="5" fill="none" stroke="#fff" stroke-width="1"/><path d="M3.6 6.2l1.7 1.6 3.2-3.4" fill="none" stroke="#fff" stroke-width="1"/></svg>Due diligence</li>
        <li><svg viewBox="0 0 12 12"><circle cx="6" cy="6" r="5" fill="none" stroke="#fff" stroke-width="1"/><path d="M3.6 6.2l1.7 1.6 3.2-3.4" fill="none" stroke="#fff" stroke-width="1"/></svg>Financing</li>
        <li><svg viewBox="0 0 12 12"><circle cx="6" cy="6" r="5" fill="none" stroke="#fff" stroke-width="1"/><path d="M3.6 6.2l1.7 1.6 3.2-3.4" fill="none" stroke="#fff" stroke-width="1"/></svg>Underwriting</li>
        <li><svg viewBox="0 0 12 12"><circle cx="6" cy="6" r="5" fill="none" stroke="#fff" stroke-width="1"/><path d="M3.6 6.2l1.7 1.6 3.2-3.4" fill="none" stroke="#fff" stroke-width="1"/></svg>Property management</li>
      </ul>
      <ul class="topics col-right">
        <li><svg viewBox="0 0 12 12"><circle cx="6" cy="6" r="5" fill="none" stroke="#fff" stroke-width="1"/><path d="M3.6 6.2l1.7 1.6 3.2-3.4" fill="none" stroke="#fff" stroke-width="1"/></svg>Real estate Legal basics</li>
        <li><svg viewBox="0 0 12 12"><circle cx="6" cy="6" r="5" fill="none" stroke="#fff" stroke-width="1"/><path d="M3.6 6.2l1.7 1.6 3.2-3.4" fill="none" stroke="#fff" stroke-width="1"/></svg>Sourcing deals</li>
        <li><svg viewBox="0 0 12 12"><circle cx="6" cy="6" r="5" fill="none" stroke="#fff" stroke-width="1"/><path d="M3.6 6.2l1.7 1.6 3.2-3.4" fill="none" stroke="#fff" stroke-width="1"/></svg>Syndication</li>
        <li><svg viewBox="0 0 12 12"><circle cx="6" cy="6" r="5" fill="none" stroke="#fff" stroke-width="1"/><path d="M3.6 6.2l1.7 1.6 3.2-3.4" fill="none" stroke="#fff" stroke-width="1"/></svg>Dealing with brokers</li>
        <li><svg viewBox="0 0 12 12"><circle cx="6" cy="6" r="5" fill="none" stroke="#fff" stroke-width="1"/><path d="M3.6 6.2l1.7 1.6 3.2-3.4" fill="none" stroke="#fff" stroke-width="1"/></svg>Tax fundamentals</li>
      </ul>
    </section>
  </div>
</body>
</html>
```